120ml Jar Label — Masculine Cosmetic Foot Balm for Cracked, Hardworking Heels

We need a print-ready wraparound label for a 120ml jar — a brown/amber glass jar with a black metal screw lid (file photo attached).

--DO NOT PUT A BARCODE ON THE LABEL PLEASE--
**PLEASE READ "PLAN HUDDLE PROJECT BRIEF FINAL.MD" IN ATTACHED FILES IF YOU ARE SUBMITTING A DESIGN.**

The label is 190mm wide × 40mm high.
We need files to be in an .ai format with a 2mm bleed at the end.
Social media handle: @bramblekeepnz (facebook, instagram and tiktok)

Bramble Keep is a New Zealand foot-care brand making practical, no-nonsense products for hardworking men whose jobs wreck their feet. Our flagship product, Ridge Mender Balm, helps fix thick, cracked, hardworking skin.

Brand color scheme and overview is all in the brief file. You may add some brand aligned colors outside of the specified hex codes as you see fit to make a great design. Feel free to remove the "Bramble Keep" text from the logo so Bramble Keep is not doubled up on the front of the label

The tone we want: direct, rugged, and credible — like a workwear brand, not a spa brand. Most cracked-heel products on the market lean soft and feminine; we want to stand apart by looking like a serious fix for a real problem, made in New Zealand.

Full legal requirements for New Zealand cosmetic labelling (ingredients, directions, net contents, origin, etc.) are listed in the attached brief document — these are non-negotiable and must stay legible.

Please see the label attached "Label spacing guide" for this project's rough spacing guide. This label is the same size and sits well on the jar. This label doesn't need to be spaced quite as much as the Verin Label

I want to run the design for a week - I feel 7 days is a good amount of time for designers to see the work, digest the brief and create something remarkable and memorable for Bramble Keep.

Target Market(s)

Working men in New Zealand whose jobs or lifestyle put heavy wear on their feet — tradies, farmers, hospital/shift workers, hunters, and outdoors people. Practical, value-driven buyers rather than luxury skincare shoppers.

Industry/Entity Type

Beauty / Health & Wellness / Cosmetics

Font styles to use
Sans Serif
Other font styles liked:
• Montserrat (bold, headings), Inter (regular, body)

Colors
00AB8E
00BBA5
67D7C9
C6EFE9
E9F9F6
FFC000
F8CF3A
FAE287
FDF2CF
FEFAEE

Requirements
Must have
• All NZ cosmetic labelling requirements from the attached brief (product name, tag line, net contents, ingredients, directions, storage, made in NZ) — legible and complete, not omitted for aesthetics Fits 190mm × 40mm wraparound format for a 120ml brown jar with black lid Uses our existing brand colors: Deep Olive #3C4A34, Bone White #F4EFE6, Terracotta Clay #C1683D, and Warm Grey #4A4540 (exact palette in attached brief) Uses Montserrat (headings) and Inter (body) or close equivalents Incorporates our existing shield-and-wing logo (attached) Brand name and product name clearly readable from a normal shelf/bathroom-cabinet distance
Nice to have
• A style that could extend into a hero/product photo later, similar to the NZ-hills-backdrop look on our website (screenshot attached) — not required for the label itself, just good to keep in mind Original icon work (e.g. a small soak/apply/sock icon set) if it fits the rugged brand feel A design that could work as a small back-label/wraparound split if the front can't fit everything at a readable size
Should not have
• No pastel colors, floral motifs, or delicate script fonts — this should never look like spa/luxury skincare. Don't introduce new brand colors outside the palette provided other than black.

```html
<!DOCTYPE html>
<html lang="en">
<head>
<meta charset="utf-8">
<title>Bramble Keep – Ridge Mender Balm Label</title>
<link rel="stylesheet" href="https://fonts.googleapis.com/css2?family=Montserrat:wght@500;600;700;800&family=Inter:wght@400;500;600&display=swap">
<style>
  :root {
    --backdrop: #ecdfd2;
    --olive: #3c4a34;
    --olive-dark: #2f3b29;
    --bone: #f4efe6;
    --terracotta: #c1683d;
    --warm-grey: #4a4540;
    --note-grey: #7a716a;
    --divider: rgba(244, 239, 230, 0.25);
  }
  * { box-sizing: border-box; margin: 0; padding: 0; }
  html, body { width: 1200px; height: 882px; overflow: hidden; }
  body {
    background: var(--backdrop);
    font-family: "Inter", sans-serif;
    position: relative;
  }

  .label {
    position: absolute;
    left: 137px; top: 180px;
    width: 957px; height: 202px;
    background: var(--olive);
    color: var(--bone);
    overflow: hidden;
  }
  .hills-art {
    position: absolute; inset: 0;
    background:
      radial-gradient(ellipse 60% 45% at 50% 70%, rgba(90,104,78,0.55), transparent 70%),
      linear-gradient(180deg, var(--olive-dark) 0%, var(--olive) 55%, #45553b 100%);
  }

  .panel { position: absolute; top: 0; height: 100%; }
  .panel--back { left: 0; width: 261px; border-right: 1px solid var(--divider); }
  .panel--front { left: 261px; width: 436px; text-align: center; }
  .panel--info { left: 697px; width: 260px; border-left: 1px solid var(--divider); }

  .heading {
    font-family: "Montserrat", sans-serif;
    font-weight: 600;
    font-size: 11px;
    line-height: 13px;
    color: var(--terracotta);
    letter-spacing: 0.02em;
  }
  .body-copy { font-size: 9px; line-height: 12px; }

  .info-block { position: absolute; left: 66px; width: 172px; }
  .info-block p + p { margin-top: 2px; }
  .info-icon {
    position: absolute; left: 10px;
    width: 40px; height: 40px;
  }
  .rule { position: absolute; left: 8px; width: 244px; height: 1px; background: var(--divider); }

  .steps {
    position: absolute; left: 6px; right: 8px; bottom: 4px;
    display: flex; justify-content: space-between;
    font-family: "Montserrat", sans-serif; font-size: 7.5px; font-weight: 500;
  }
  .step { display: flex; flex-direction: column; align-items: center; gap: 2px; }
  .step svg { width: 17px; height: 17px; }

  .brand-mark {
    position: absolute; left: 0; right: 0; top: 10px;
    display: flex; flex-direction: column; align-items: center; gap: 8px;
  }
  .brand-mark__dot {
    width: 46px; height: 46px; border-radius: 50%;
    border: 2px solid var(--bone); background: var(--terracotta);
  }
  .brand-name {
    font-family: "Montserrat", sans-serif; font-weight: 700;
    font-size: 12px; line-height: 14px; letter-spacing: 0.04em; color: var(--bone);
  }
  .product-name {
    position: absolute; left: 0; right: 0; top: 94px;
    font-family: "Montserrat", sans-serif; font-weight: 800;
    font-size: 28px; letter-spacing: 0.01em; line-height: 28px;
  }
  .tagline {
    position: absolute; left: 0; right: 0; top: 130px;
    display: flex; align-items: center; justify-content: center; gap: 8px;
    font-family: "Montserrat", sans-serif; font-weight: 600;
    font-size: 12px; line-height: 14px; letter-spacing: 0.14em; color: var(--terracotta);
  }
  .tagline::before, .tagline::after {
    content: ""; width: 24px; height: 1.5px; background: var(--terracotta);
  }
  .claims {
    position: absolute; left: 0; right: 0; top: 158px;
    font-family: "Montserrat", sans-serif; font-weight: 600;
    font-size: 11px; line-height: 14px; letter-spacing: 0.1em;
  }
  .net-contents {
    position: absolute; left: 50%; bottom: 0; transform: translateX(-50%);
    height: 18px; line-height: 18px;
    background: var(--terracotta);
    font-family: "Montserrat", sans-serif; font-weight: 600; font-size: 11.5px;
    padding: 0 12px;
  }

  .ingredients { position: absolute; left: 24px; top: 5px; width: 202px; }
  .ingredients .body-copy { margin-top: 4px; font-size: 8.8px; line-height: 12.7px; }
  .panel--info .rule { left: 24px; width: 194px; }
  .origin {
    position: absolute; left: 24px; top: 124px;
    display: flex; align-items: center; gap: 14px;
    font-family: "Montserrat", sans-serif; font-weight: 600; font-size: 11px; line-height: 13px;
  }
  .origin__art {
    width: 34px; height: 22px; border-radius: 12px 2px 12px 2px;
    background: linear-gradient(90deg, rgba(244,239,230,0.9), rgba(244,239,230,0.5));
  }
  .socials {
    position: absolute; left: 26px; top: 166px;
    display: flex; align-items: center; gap: 12px;
    font-family: "Montserrat", sans-serif; font-weight: 600; font-size: 13px; line-height: 22px;
  }
  .socials__dot { width: 22px; height: 22px; border-radius: 50%; background: var(--bone); }

  .brief-notes {
    position: absolute; left: 605px; top: 614px; width: 490px;
    color: var(--note-grey);
  }
  .brief-notes h2 { font-family: "Inter", sans-serif; font-weight: 500; font-size: 14px; margin-bottom: 4px; }
  .brief-notes li { list-style: none; font-size: 10px; line-height: 12px; margin-bottom: 4.5px; }
</style>
</head>
<body>

<section class="label" aria-label="Ridge Mender Balm wraparound jar label">
  <div class="hills-art" role="img" aria-label="Engraved New Zealand hill landscape backdrop in olive tones"></div>

  <div class="panel panel--back">
    <svg class="info-icon" style="top:8px" viewBox="0 0 42 42" aria-hidden="true">
      <circle cx="21" cy="21" r="19" fill="none" stroke="var(--terracotta)" stroke-width="1.5"/>
      <circle cx="21" cy="21" r="8" fill="var(--bone)"/>
    </svg>
    <div class="info-block" style="top:4px">
      <h3 class="heading">DIRECTIONS</h3>
      <div class="body-copy">
        <p>Apply generously to clean, dry feet, focusing on heels and thick or cracked areas.</p>
        <p>For cracked heels, wear our moisture-locking socks overnight.</p>
        <p>Use daily.</p>
      </div>
    </div>
    <div class="rule" style="top:99px"></div>
    <svg class="info-icon" style="top:110px" viewBox="0 0 42 42" aria-hidden="true">
      <circle cx="21" cy="21" r="19" fill="none" stroke="var(--terracotta)" stroke-width="1.5"/>
      <circle cx="21" cy="21" r="5" fill="var(--bone)"/>
      <g stroke="var(--bone)" stroke-width="1.6" stroke-linecap="round">
        <line x1="21" y1="10" x2="21" y2="13"/><line x1="21" y1="29" x2="21" y2="32"/>
        <line x1="10" y1="21" x2="13" y2="21"/><line x1="29" y1="21" x2="32" y2="21"/>
        <line x1="13.5" y1="13.5" x2="15.5" y2="15.5"/><line x1="26.5" y1="26.5" x2="28.5" y2="28.5"/>
        <line x1="13.5" y1="28.5" x2="15.5" y2="26.5"/><line x1="26.5" y1="15.5" x2="28.5" y2="13.5"/>
      </g>
    </svg>
    <div class="info-block" style="top:109px">
      <h3 class="heading">STORAGE</h3>
      <div class="body-copy">
        <p>Keep out of direct sunlight.</p>
        <p>Best used within six months of opening.</p>
      </div>
    </div>
    <div class="rule" style="top:165px"></div>
    <div class="steps">
      <div class="step">
        <svg viewBox="0 0 18 18" aria-hidden="true"><circle cx="9" cy="9" r="7" fill="none" stroke="var(--bone)" stroke-width="1.2"/></svg>
        <span>1. CLEAN</span>
      </div>
      <div class="step">
        <svg viewBox="0 0 18 18" aria-hidden="true"><rect x="3" y="5" width="12" height="9" rx="2" fill="none" stroke="var(--bone)" stroke-width="1.2"/></svg>
        <span>2. APPLY</span>
      </div>
      <div class="step">
        <svg viewBox="0 0 18 18" aria-hidden="true"><path d="M3 13 L9 13 L15 9" fill="none" stroke="var(--bone)" stroke-width="1.2" stroke-linecap="round"/></svg>
        <span>3. WEAR OVERNIGHT</span>
      </div>
    </div>
  </div>

  <div class="panel panel--front">
    <div class="brand-mark">
      <span class="brand-mark__dot" aria-hidden="true"></span>
      <span class="brand-name">BRAMBLE KEEP</span>
    </div>
    <h1 class="product-name">RIDGE MENDER BALM</h1>
    <p class="tagline">FOR HARDWORKING SOLES</p>
    <p class="claims">REPAIRS THICK · CRACKED · DRY SKIN</p>
    <span class="net-contents">120ml</span>
  </div>

  <div class="panel panel--info">
    <div class="ingredients">
      <h3 class="heading">INGREDIENTS</h3>
      <p class="body-copy">Shea Butter, Beef Tallow, Beeswax, Grape Seed Oil, Vegetable Glycerin, Lanolin, Panthenol, Gluconolactone, Sodium Benzoate, Allantoin, Manuka Honey, Vitamin E, Tea Tree Essential Oil, Lemon Myrtle Essential Oil, Rosemary Oleoresin Extract</p>
    </div>
    <div class="rule" style="top:117px"></div>
    <div class="origin">
      <span class="origin__art" role="img" aria-label="Silver fern motif"></span>
      <span>MADE IN<br>NEW ZEALAND</span>
    </div>
    <div class="rule" style="top:156px"></div>
    <div class="socials">
      <span class="socials__dot" aria-hidden="true"></span>
      <span class="socials__dot" aria-hidden="true"></span>
      <span class="socials__dot" aria-hidden="true"></span>
      <span>@bramblekeepnz</span>
    </div>
  </div>
</section>

<section class="brief-notes">
  <h2>Why this concept fits the client's brief</h2>
  <ul>
    <li>Masculine, rugged workwear aesthetic (not spa-like)</li>
    <li>Uses the specified brand colors (Deep Olive, Bone White, Terracotta, Warm Grey)</li>
    <li>Montserrat for headings and Inter for body copy</li>
    <li>Front-facing branding is large and highly legible</li>
    <li>Wraparound layout keeps secondary information on the curved sides</li>
    <li>Includes all required NZ cosmetic label information: product name, tagline, net contents, directions, ingredients, storage, and "Made in New Zealand"</li>
    <li>No barcode</li>
    <li>Easy to extend into future product photography and website hero images with the same New Zealand landscape styling.</li>
  </ul>
</section>

</body>
</html>
```